stars + comments Reviews website design (similar to grubly concept)

Please refer to attached logo and wire frames
----------------------------------------------------------------------------------------------------
we are a company based in egypt, seeking a design for a website that allows user to find doctors using search and filters.
also it allows user to review this doctor through providing comment and 1 to 5 stars
i need 4 main pages designs:
1- Doctors list/favorites list
2- Doctor view
3- Add doctor (3 steps)
4- Sign-in/sign up
5- Menu design
am into the colors teal/turquoise (though am open for different opinion)
i don't want the design theme to be doctors specific
am into the school of very clean, very neat, very simple
(chirpnet, pagecircle, snapmosaic designs are appealing to me)
Updates

Number of Pages Required

4 page

Font styles to use
Sans Serif

Colors
00a990
33b8a4

Requirements
Must have
• website will be bilingual/ bi-directional (English and Arabic)
• designer needs to provide another copy of the design with "right to left" orientation
• interactive button animation

```html
<!DOCTYPE html>
<html lang="en">
<head>
<meta charset="utf-8">
<title>Curavia – Find Doctors</title>
<link href="https://fonts.googleapis.com/css2?family=Source+Sans+3:wght@400;600;700&display=swap" rel="stylesheet">
<style>
:root{
  --teal:#009697;
  --teal-dark:#006e70;
  --teal-soft:#0aa3a3;
  --ink:#333;
  --muted:#777;
  --line:#cfd6d6;
  --star:#f7b500;
  --footer:#e2e2e2;
  --white:#fff;
}
*{box-sizing:border-box;margin:0;padding:0}
html,body{width:1120px;height:1200px;overflow:hidden;background:var(--white);font-family:"Source Sans 3",sans-serif;color:var(--ink)}
.page{position:relative;width:1120px;height:1200px;overflow:hidden}
.abs{position:absolute}

.site-header{position:absolute;left:0;top:0;width:1120px;height:72px;background:var(--teal)}
.brand{position:absolute;left:92px;top:16px;color:var(--white);font-size:36px;font-weight:700;line-height:40px;display:flex;align-items:center;gap:10px}
.brand-dot{width:22px;height:22px;background:var(--white);border-radius:50%}
.nav-icon{position:absolute;top:24px;width:28px;height:26px}
.signin{position:absolute;left:947px;top:23px;width:82px;height:26px;border:1px solid var(--white);display:flex}
.signin span{flex:1;background:var(--white);color:var(--teal);font-size:11px;line-height:24px;padding-left:8px}
.signin i{width:25px;display:flex;align-items:center;justify-content:center}

.hero{position:absolute;left:0;top:72px;width:1120px;height:360px;background:linear-gradient(100deg,#e9ecee 0%,#dfe4e6 35%,#f2f4f5 55%,#9cc9d9 78%,#e6e9ea 100%)}
.hero-title{position:absolute;left:91px;top:196px;height:56px;padding:0 12px;background:var(--teal);color:var(--white);font-size:31px;font-weight:700;line-height:56px}
.hero-sub{position:absolute;left:91px;top:252px;width:424px;height:56px;background:var(--teal-dark);color:var(--white);font-size:25px;line-height:56px;padding-left:13px}
.hero-cta{position:absolute;left:91px;top:316px;width:185px;height:39px;background:var(--teal);color:var(--white);font-size:14px;font-weight:700;line-height:39px;text-align:center}
.dots{position:absolute;left:541px;top:411px;display:flex;gap:2px}
.dots b{width:13px;height:13px;background:var(--teal-dark)}
.dots b:nth-child(2){background:#0b5f63}
.dots b:last-child{background:var(--teal)}

.filter{position:absolute;top:481px;width:137px;height:32px;border:1px solid var(--teal);display:flex;background:var(--white)}
.filter span{flex:1;font-size:10px;color:var(--muted);line-height:30px;padding-left:7px;white-space:nowrap;overflow:hidden}
.filter i{width:32px;background:var(--teal);display:flex;align-items:center;justify-content:center}

.section-title{position:absolute;top:550px;font-size:16px;font-weight:600;color:#222}

.doctor-list{position:absolute;left:91px;top:574px;width:617px;height:413px;border:1px solid var(--teal)}
.doctor{position:relative;height:103px;border-bottom:1px solid var(--teal)}
.doctor:last-child{border-bottom:0}
.doctor.active{background:#f3f3f3}
.photo{position:absolute;left:8px;top:11px;width:80px;height:80px;background:linear-gradient(135deg,#eef1f2,#b9c6cc)}
.doc-name{position:absolute;left:105px;top:20px;font-size:14px;color:var(--teal);font-weight:600}
.doc-name small{font-size:11px;color:var(--muted);font-weight:400}
.doc-spec{position:absolute;left:105px;top:40px;font-size:12px;color:#555}
.doc-addr{position:absolute;left:105px;top:64px;font-size:13px;color:#444}
.rating{position:absolute;right:14px;top:14px;display:flex;align-items:center;gap:3px;font-size:11px;color:#444}
.rating svg{width:18px;height:18px}
.fav{position:absolute;right:14px;top:65px;width:26px;height:24px}

.reviews{position:absolute;left:731px;top:574px;width:297px;height:319px;border:1px solid var(--line)}
.review{position:relative;height:159px;border-bottom:1px solid var(--line)}
.review:last-child{border-bottom:0}
.review .photo{left:8px;top:12px}
.rv-name{position:absolute;left:96px;top:22px;font-size:13px;font-weight:600;color:var(--teal);white-space:nowrap}
.rv-name small{font-size:11px;color:var(--muted);font-weight:400}
.rv-spec{position:absolute;left:96px;top:41px;font-size:12px;color:#555}
.review .rating{left:96px;right:auto;top:60px}
.review .fav{right:24px;top:76px;width:24px;height:22px}
.rv-by{position:absolute;left:96px;top:88px;font-size:12px;font-weight:600;color:var(--teal)}
.rv-text{position:absolute;left:96px;top:105px;width:195px;font-size:9.5px;line-height:14px;color:#444}
.rv-text a{color:var(--teal);text-decoration:none}

.site-footer{position:absolute;left:0;top:1011px;width:1120px;height:150px;background:var(--footer)}
.site-footer .brand{color:var(--teal);top:36px}
.site-footer .brand-dot{background:var(--teal)}
.social{position:absolute;left:92px;top:107px;display:flex;gap:8px}
.social b{width:25px;height:25px;background:var(--teal)}
.contact{position:absolute;left:812px;top:22px}
.contact h3{font-size:17px;font-weight:400;color:var(--teal);margin-bottom:14px}
.contact p{display:flex;align-items:center;gap:12px;font-size:12px;color:#444;height:25px}
.contact svg{width:12px;height:12px}
.copyright{position:absolute;left:0;top:1161px;width:1120px;height:39px;background:var(--footer);border-top:1px solid #cfcfcf;text-align:center;font-size:10px;line-height:38px;color:#444}
</style>
</head>
<body>
<svg width="0" height="0" style="position:absolute">
  <defs>
    <symbol id="star" viewBox="0 0 24 24"><path d="M12 2l3 6.6 7.2.8-5.4 4.9 1.5 7.1L12 17.8 5.7 21.4l1.5-7.1L1.8 9.4 9 8.6z" fill="#f7b500"/></symbol>
    <symbol id="star-half" viewBox="0 0 24 24"><path d="M12 2l3 6.6 7.2.8-5.4 4.9 1.5 7.1L12 17.8 5.7 21.4l1.5-7.1L1.8 9.4 9 8.6z" fill="none" stroke="#f7b500" stroke-width="2"/><path d="M12 2v15.8L5.7 21.4l1.5-7.1L1.8 9.4 9 8.6z" fill="#f7b500"/></symbol>
    <symbol id="heart" viewBox="0 0 26 24"><path d="M13 22S2 15 2 8a5.5 5.5 0 0 1 11-1 5.5 5.5 0 0 1 11 1c0 7-11 14-11 14z" fill="none" stroke="#009697" stroke-width="2"/></symbol>
    <symbol id="heart-full" viewBox="0 0 26 24"><path d="M13 22S2 15 2 8a5.5 5.5 0 0 1 11-1 5.5 5.5 0 0 1 11 1c0 7-11 14-11 14z" fill="#009697" stroke="#009697" stroke-width="2"/></symbol>
    <symbol id="caret" viewBox="0 0 12 8"><path d="M1 1l5 5 5-5" fill="none" stroke="#fff" stroke-width="2"/></symbol>
  </defs>
</svg>

<div class="page">
  <header class="site-header">
    <div class="brand"><span class="brand-dot"></span>Curavia</div>
    <svg class="nav-icon" style="left:666px" viewBox="0 0 28 26"><path d="M14 2L2 13h4v11h6v-7h4v7h6V13h4z" fill="#006e70"/></svg>
    <svg class="nav-icon" style="left:747px" viewBox="0 0 26 24"><path d="M13 22S2 15 2 8a5.5 5.5 0 0 1 11-1 5.5 5.5 0 0 1 11 1c0 7-11 14-11 14z" fill="#fff"/></svg>
    <svg class="nav-icon" style="left:827px" viewBox="0 0 28 26"><circle cx="11" cy="8" r="5" fill="#fff"/><path d="M2 24c0-6 4-9 9-9s9 3 9 9z" fill="#fff"/><path d="M22 9v8M18 13h8" stroke="#fff" stroke-width="2.5"/></svg>
    <div class="signin"><span>Sign In</span><i><svg width="10" height="6" viewBox="0 0 10 6"><path d="M0 0h10L5 6z" fill="#fff"/></svg></i></div>
  </header>

  <section class="hero" role="img" aria-label="Photo of a smiling team of doctors and nurses in a bright hospital hall"></section>
  <div class="hero-title">Curavia</div>
  <div class="hero-sub">is the best way to find graet Doctors</div>
  <div class="hero-cta">Create Your Free Account</div>
  <div class="dots"><b></b><b></b><b></b></div>

  <div class="filter" style="left:91px"><span>Search Here...</span><i><svg width="13" height="13" viewBox="0 0 14 14"><circle cx="6" cy="6" r="4.3" fill="none" stroke="#fff" stroke-width="2"/><path d="M9 9l4 4" stroke="#fff" stroke-width="2.4"/></svg></i></div>
  <div class="filter" style="left:251px"><span>Specialization...</span><i><svg width="12" height="8"><use href="#caret"/></svg></i></div>
  <div class="filter" style="left:411px"><span>Sub-Specialization...</span><i><svg width="12" height="8"><use href="#caret"/></svg></i></div>
  <div class="filter" style="left:571px"><span>Area...</span><i><svg width="12" height="8"><use href="#caret"/></svg></i></div>
  <div class="filter" style="left:731px"><span>Gender...</span><i><svg width="12" height="8"><use href="#caret"/></svg></i></div>
  <div class="filter" style="left:891px"><span>Rating...</span><i><svg width="12" height="8"><use href="#caret"/></svg></i></div>

  <h2 class="section-title" style="left:92px">15,123 Doctors</h2>
  <h2 class="section-title" style="left:731px">Reviews of the Day</h2>

  <div class="doctor-list">
    <div class="doctor active">
      <div class="photo" role="img" aria-label="Portrait of the doctor"></div>
      <div class="doc-name">Dr. Samir Adel <small>(1 km away)</small></div>
      <div class="doc-spec">Anesthesiologist</div>
      <div class="doc-addr">73 Cedar Street, Westbank.</div>
      <div class="rating"><svg><use href="#star"/></svg><svg><use href="#star"/></svg><svg><use href="#star"/></svg><svg><use href="#star"/></svg><svg><use href="#star-half"/></svg>&nbsp;( 130 )</div>
      <svg class="fav"><use href="#heart"/></svg>
    </div>
    <div class="doctor">
      <div class="photo" role="img" aria-label="Portrait of the doctor"></div>
      <div class="doc-name">Dr. Lina Farouk <small>(9 km away)</small></div>
      <div class="doc-spec">Dentist</div>
      <div class="doc-addr">48 Olive Street, Eastgate.</div>
      <div class="rating"><svg><use href="#star"/></svg><svg><use href="#star"/></svg><svg><use href="#star"/></svg><svg><use href="#star"/></svg><svg><use href="#star-half"/></svg>&nbsp;( 160 )</div>
      <svg class="fav"><use href="#heart-full"/></svg>
    </div>
    <div class="doctor">
      <div class="photo" role="img" aria-label="Portrait of the doctor"></div>
      <div class="doc-name">Dr. Hana Karim <small>(8 km away)</small></div>
      <div class="doc-spec">Pediatrician</div>
      <div class="doc-addr">122 Palm Street, Westbank.</div>
      <div class="rating"><svg><use href="#star"/></svg><svg><use href="#star"/></svg><svg><use href="#star"/></svg><svg><use href="#star"/></svg><svg><use href="#star-half"/></svg>&nbsp;( 260 )</div>
      <svg class="fav"><use href="#heart"/></svg>
    </div>
    <div class="doctor">
      <div class="photo" role="img" aria-label="Portrait of the doctor"></div>
      <div class="doc-name">Dr. Hana Karim <small>(8 km away)</small></div>
      <div class="doc-spec">Pediatrician</div>
      <div class="doc-addr">122 Palm Street, Westbank.</div>
      <div class="rating"><svg><use href="#star"/></svg><svg><use href="#star"/></svg><svg><use href="#star"/></svg><svg><use href="#star"/></svg><svg><use href="#star-half"/></svg>&nbsp;( 120 )</div>
      <svg class="fav"><use href="#heart"/></svg>
    </div>
  </div>

  <div class="reviews">
    <div class="review">
      <div class="photo" role="img" aria-label="Portrait of the reviewed doctor"></div>
      <div class="rv-name">Dr. Samir <small>( reviewed )</small> Jon Parker</div>
      <div class="rv-spec">Anesthesiologist</div>
      <div class="rating"><svg><use href="#star"/></svg><svg><use href="#star"/></svg><svg><use href="#star"/></svg><svg><use href="#star"/></svg><svg><use href="#star-half"/></svg></div>
      <svg class="fav"><use href="#heart"/></svg>
      <div class="rv-by">Jon Parker...!</div>
      <p class="rv-text">Lorem Ipsum is simply dummy text of the printing and typesetting industry. Lorem Ipsum &nbsp;<a href="#">Read more...</a></p>
    </div>
    <div class="review">
      <div class="photo" role="img" aria-label="Portrait of the reviewed doctor"></div>
      <div class="rv-name">Dr. Lina <small>( reviewed )</small> Jon Parker</div>
      <div class="rv-spec">Anesthesiologist</div>
      <div class="rating"><svg><use href="#star"/></svg><svg><use href="#star"/></svg><svg><use href="#star"/></svg><svg><use href="#star"/></svg><svg><use href="#star-half"/></svg></div>
      <svg class="fav"><use href="#heart"/></svg>
      <div class="rv-by">Jon Parker...!</div>
      <p class="rv-text">Lorem Ipsum is simply dummy text of the printing and typesetting industry. Lorem Ipsum &nbsp;<a href="#">Read more...</a></p>
    </div>
  </div>

  <footer class="site-footer">
    <div class="brand"><span class="brand-dot"></span>Curavia</div>
    <div class="social" aria-label="Social links"><b></b><b></b><b></b></div>
    <div class="contact">
      <h3>Contact Us</h3>
      <p><svg viewBox="0 0 12 12"><path d="M2 1l2.5 0 1 3-1.5 1a6 6 0 0 0 3 3l1-1.5 3 1V10c0 .6-.5 1-1 1A9 9 0 0 1 1 2c0-.5.4-1 1-1z" fill="#444"/></svg>555 010 200</p>
      <p><svg viewBox="0 0 12 12"><rect x="0.5" y="2" width="11" height="8" fill="#444"/><path d="M1 2.5l5 4 5-4" fill="none" stroke="#e2e2e2"/></svg>info@curavia.com</p>
      <p><svg viewBox="0 0 12 12"><path d="M6 11S2 7 2 4.5a4 4 0 0 1 8 0C10 7 6 11 6 11z" fill="#444"/><circle cx="6" cy="4.5" r="1.4" fill="#e2e2e2"/></svg>Curavia</p>
    </div>
  </footer>
  <div class="copyright">Copyrights © 2015 Curavia</div>
</div>
</body>
</html>
```